"Torvek Industries" needs a creative design

We need a Business card design for a new company based in Australia : Melbourne called "Torvek Industries"

The company will primary be importing Furniture . ie Replica Furniture, Home furniture, Office Furniture, Outdoor Furniture and Entertainment Units

We would like to see the design that use the color Champion Red / Platinum Silver on the Logo .

The final design should communicate " Great quality furniture, Best prices and good customer service"

Also in the Business card please add the following info
- ABN : 52384017265
- Email Address : Torvek.Industires@Mailpoint.com
- WebSite : www.TorvekIndustries.com.au
- FB (facebook icon) : [TorvekIndustries] Like us on Facebook [like hand]
- PH : 0472 916 358

Please refer to attachment for the logo

Sans Serif

eb1f27
1b1b1b
5c5c5c
f5f5f5
f04a50

```html
<!DOCTYPE html>
<html lang="en">
<head>
<meta charset="utf-8">
<title>Torvek Industries – Business Card</title>
<link href="https://fonts.googleapis.com/css2?family=Archivo:wght@700;800&family=Open+Sans:wght@400&display=swap" rel="stylesheet">
<style>
  :root {
    --champion-red: #eb1f27;
    --ink: #1b1b1b;
    --graphite: #5c5c5c;
    --paper: #ffffff;
    --backdrop: #f5f5f5;
  }
  * { box-sizing: border-box; margin: 0; padding: 0; }
  html, body { width: 1200px; height: 900px; overflow: hidden; }
  body {
    background: var(--backdrop);
    display: flex;
    align-items: center;
    justify-content: center;
    gap: 48px;
    font-family: "Archivo", Arial, sans-serif;
  }
  .card {
    width: 520px;
    height: 295px;
    position: relative;
    overflow: hidden;
    box-shadow: 0 2px 10px rgba(0,0,0,0.12);
  }

  /* Back side */
  .card--back {
    background: var(--ink);
    display: flex;
    align-items: center;
    justify-content: center;
  }
  .brand {
    display: flex;
    align-items: center;
    gap: 14px;
  }
  .brand__square {
    width: 20px;
    height: 20px;
    background: var(--champion-red);
    flex: none;
  }
  .brand__name {
    font-weight: 800;
    text-transform: uppercase;
    line-height: 1.02;
    letter-spacing: 0.01em;
  }
  .card--back .brand__name { color: var(--paper); font-size: 40px; }

  /* Front side */
  .card--front { background: var(--paper); }
  .card--front .brand {
    position: absolute;
    top: 26px;
    left: 18px;
    gap: 10px;
  }
  .card--front .brand__square { width: 16px; height: 16px; }
  .card--front .brand__name { color: var(--ink); font-size: 25px; }

  .name-band {
    position: absolute;
    top: 129px;
    left: 0;
    right: 0;
    height: 61px;
    display: flex;
    gap: 6px;
  }
  .name-band__accent { width: 147px; background: var(--champion-red); }
  .name-band__bar {
    flex: 1;
    background: var(--ink);
    color: var(--paper);
    display: flex;
    align-items: center;
    justify-content: flex-end;
    padding-right: 16px;
    font-family: "Open Sans", Arial, sans-serif;
    font-size: 26px;
    font-weight: 400;
  }

  .contact {
    position: absolute;
    left: 18px;
    top: 212px;
    list-style: none;
    color: var(--ink);
    font-weight: 700;
    font-size: 15px;
    line-height: 26px;
  }
  .contact__abn { font-size: 16px; }
</style>
</head>
<body>
  <section class="card card--back" aria-label="Card back">
    <div class="brand">
      <span class="brand__square"></span>
      <span class="brand__name">Torvek<br>Industries</span>
    </div>
  </section>

  <section class="card card--front" aria-label="Card front">
    <div class="brand">
      <span class="brand__square"></span>
      <span class="brand__name">Torvek<br>Industries</span>
    </div>
    <div class="name-band">
      <div class="name-band__accent"></div>
      <div class="name-band__bar">Dana Whitlock</div>
    </div>
    <ul class="contact">
      <li class="contact__abn">52384017265</li>
      <li>Torvek.Industires@Mailpoint.com</li>
      <li>www.TorvekIndustries.com.au</li>
    </ul>
  </section>
</body>
</html>
```